Business card for Chicago based Private Equity Company

We need a business card for our PE company called Crestline Partners. We want a simple and clean, yet creative card design. The back side should reflect our logo. Also would like to see embossed ideas. Should reflect strength and growth. Our logo is attached. Also need editable file. Details are as follows for Business Card:

Dale Moravec Co-Founder 2750 Larkin Avenue Suite 410 Oak Brook, IL 60587 http://www.crestlinepartnersllc.example (D) 630.555.0142 (C) 312.555.0178 (E) dm@crestlinepartnersllc.example

```html
<!DOCTYPE html>
<html lang="en">
<head>
<meta charset="utf-8">
<title>Crestline Partners – Business Card</title>
<link rel="stylesheet" href="https://fonts.googleapis.com/css2?family=Quicksand:wght@500&display=swap">
<style>
  :root {
    --backdrop: #d9dadc;
    --card-white: #ffffff;
    --ink: #1a1a1a;
    --card-black: #000000;
    --accent-red: #b3171d;
    --reverse-text: #ffffff;
  }
  html, body {
    margin: 0;
    width: 1200px;
    height: 1200px;
    overflow: hidden;
    background: var(--backdrop);
    font-family: "Quicksand", "Helvetica Neue", Arial, sans-serif;
    font-weight: 500;
  }
  .canvas { position: relative; width: 1200px; height: 1200px; }
  .card {
    position: absolute;
    left: 228px;
    width: 742px;
    height: 422px;
    overflow: hidden;
  }
  .card-front { top: 170px; background: var(--card-white); color: var(--ink); }
  .card-back { top: 602px; background: var(--card-black); color: var(--reverse-text); }

  .brand-name {
    position: absolute;
    left: 28px;
    top: 64px;
    margin: 0;
    font-size: 34px;
    line-height: 1;
    letter-spacing: 2px;
    text-transform: uppercase;
    font-weight: 500;
    color: var(--ink);
    white-space: nowrap;
  }

  .person { position: absolute; left: 71px; top: 250px; }
  .person-name { margin: 0; font-size: 31px; font-weight: 500; line-height: 1.1; }
  .person-title { margin: 0; font-size: 21px; line-height: 1.2; }

  .contact-list {
    position: absolute;
    left: 383px;
    top: 198px;
    margin: 0;
    padding: 0;
    list-style: none;
    font-size: 19.5px;
    line-height: 29px;
  }
  .contact-list li { display: flex; align-items: flex-start; }
  .contact-list li.gap { margin-top: 18px; }
  .contact-icon { width: 16px; height: 16px; margin: 6px 10px 0 0; flex: none; fill: var(--accent-red); }
  .contact-address span { display: block; }

  .front-band { position: absolute; left: 0; bottom: 0; width: 742px; height: 48px; }
  .front-band polygon { fill: var(--card-black); }

  .back-brand {
    position: absolute;
    left: 479px;
    top: 250px;
    margin: 0;
    transform: translateX(-50%);
    white-space: nowrap;
    font-size: 22px;
    letter-spacing: 3px;
    text-transform: uppercase;
    font-weight: 500;
    color: var(--reverse-text);
  }
  .back-web {
    position: absolute;
    right: 27px;
    bottom: 20px;
    margin: 0;
    font-size: 20px;
    color: var(--reverse-text);
  }
</style>
</head>
<body>
<div class="canvas">

  <section class="card card-front" aria-label="Card front">
    <h1 class="brand-name">Crestline Partners</h1>

    <div class="person">
      <p class="person-name">Dale Moravec</p>
      <p class="person-title">Co-Founder</p>
    </div>

    <ul class="contact-list">
      <li class="contact-address">
        <svg class="contact-icon" viewBox="0 0 16 16" aria-hidden="true"><path d="M8 1 0 8h2v7h4v-4h4v4h4V8h2z"/></svg>
        <div><span>2750 Larkin Avenue Suite 410</span><span>Oak Brook, IL 60587</span></div>
      </li>
      <li class="gap">
        <svg class="contact-icon" viewBox="0 0 16 16" aria-hidden="true"><path d="M3 1l3 3-2 2c1 2 3 4 6 6l2-2 3 3-2 2C7 15 1 9 1 3z"/></svg>
        <span>630.555.0142</span>
      </li>
      <li>
        <svg class="contact-icon" viewBox="0 0 16 16" aria-hidden="true"><path d="M4 0h8v16H4zM5.5 2v9h5V2z"/></svg>
        <span>312.555.0178</span>
      </li>
      <li>
        <svg class="contact-icon" viewBox="0 0 16 16" aria-hidden="true"><path d="M0 3h16v1L8 9 0 4zM0 6l8 5 8-5v7H0z"/></svg>
        <span>dm@crestlinepartnersllc.example</span>
      </li>
      <li>
        <svg class="contact-icon" viewBox="0 0 16 16" aria-hidden="true"><path d="M8 0a8 8 0 1 0 0 16A8 8 0 0 0 8 0zm0 1.5c1 1 1.7 3 1.8 5.5H6.2C6.3 4.5 7 2.5 8 1.5zM4.7 7H1.6a6.5 6.5 0 0 1 4-5.2C5 3.2 4.7 5 4.7 7zm6.6 0c0-2-.4-3.8-1-5.2a6.5 6.5 0 0 1 4 5.2zM1.6 8.5h3.1c0 2 .4 3.7 1 5.2a6.5 6.5 0 0 1-4.1-5.2zm4.6 0h3.6c-.1 2.5-.8 4.5-1.8 5.5-1-1-1.7-3-1.8-5.5zm5.1 0h3.1a6.5 6.5 0 0 1-4 5.2c.5-1.5.9-3.2.9-5.2z"/></svg>
        <span>www.crestlinepartnersllc.example</span>
      </li>
    </ul>

    <svg class="front-band" viewBox="0 0 742 48" aria-hidden="true">
      <polygon points="0,0 354,0 372,22 742,22 742,48 0,48"/>
    </svg>
  </section>

  <section class="card card-back" aria-label="Card back">
    <p class="back-brand">Crestline Partners</p>
    <p class="back-web">www.crestlinepartnersllc.example</p>
  </section>

</div>
</body>
</html>
```